TIMBER DECK COMPANY FLYER

We need a flyer design for a Timber Decking company, we specialise in timber decks, stairs, privacy screens, maintenance and pergolas. I have attatched some pictures which you can incorporate if you think they need cropping go for it. We offer amazing decks at affordable prices by qualified tradespeople.
My logo is a dull green I would like this to be changed to a more lime bright green please. Also my logo is too big I would like this logo halved in size please. And the colours in the brochure maybe a blackbackground with lime green and other colours you think will work. We will also beat any reputable Decking companies quote by 10%. Our decks add style, class, longjevity and practicality to any home. The final design should be modern and cutting edge.

Target Market(s)

home owners

Industry/Entity Type

It Company

Logo Text

CRISP PLANKWORKS GROUP

Requirements
Must have
• DECKS
STAIRS
PERGOLAS
PRIVACY SCREENS
DECK MAINTENANCE

CONTACT-GORDON-0438261507

MUST HAVE LIKE US ON PAGEBOARD LOGO

www.crispplankworksgroup.com.au
Nice to have
• Please let me know if need more photos etc

```html
<!DOCTYPE html>
<html lang="en">
<head>
<meta charset="utf-8">
<title>Crisp Plankworks Group – Flyer</title>
<link rel="stylesheet" href="https://fonts.googleapis.com/css2?family=Archivo+Black&family=Roboto+Condensed:wght@700&display=swap">
<style>
  :root {
    --lime: #c9e41c;
    --lime-light: #d9ee4a;
    --black: #111111;
    --white: #ffffff;
    --timber-dark: #7a5a44;
    --timber-mid: #a88668;
    --timber-light: #c9b08e;
    --ink: #1c1c1c;
  }
  * { box-sizing: border-box; margin: 0; padding: 0; }
  html, body { width: 1200px; height: 930px; overflow: hidden; background: var(--lime); }
  .flyer {
    position: relative;
    width: 1200px;
    height: 930px;
    background: var(--lime);
    font-family: "Roboto Condensed", "Arial Narrow", sans-serif;
    overflow: hidden;
  }
  .hero-deck {
    position: absolute; left: 0; top: 0; width: 1200px; height: 260px;
    background: linear-gradient(180deg, var(--timber-mid) 0%, var(--timber-light) 55%, var(--lime-light) 88%, var(--lime) 100%);
  }
  .brand {
    position: absolute; left: 48px; top: 44px; width: 1110px; height: 150px;
    display: flex; align-items: center; gap: 46px;
  }
  .brand-square { width: 140px; height: 140px; background: var(--black); flex: none; }
  .brand-name {
    font-family: "Archivo Black", "Arial Black", sans-serif;
    color: var(--black);
    line-height: 1;
  }
  .brand-name .line-one { display: block; font-size: 74px; letter-spacing: -1px; }
  .brand-name .line-two { display: block; font-size: 56px; letter-spacing: 32px; margin-top: 10px; }
  .services {
    position: absolute; left: 0; top: 246px; width: 1200px;
    text-align: center; color: var(--white);
    font-size: 64px; line-height: 78px; letter-spacing: 0.5px;
    text-shadow: 2px 3px 6px rgba(0,0,0,0.35);
  }
  .gallery {
    position: absolute; left: 0; top: 430px; width: 1200px; height: 243px;
    display: flex; gap: 4px; background: var(--white);
  }
  .gallery .photo { height: 100%; }
  .photo-pool-deck { width: 288px; background: linear-gradient(180deg, #6f7a4a 0%, #7d4630 45%, #5e2f1f 100%); }
  .photo-pool-walk { width: 322px; background: linear-gradient(90deg, #4f6b33 0%, #8a5a3c 35%, #5aa9c8 70%, #5b7a36 100%); }
  .photo-plunge { width: 320px; background: linear-gradient(180deg, #4b4e4c 0%, #2a4646 45%, #8b3a22 100%); }
  .photo-stairs { flex: 1; background: linear-gradient(90deg, #3f6a2e 0%, #5f7f3a 40%, #d8c6a3 100%); }
  .offer-band {
    position: absolute; left: 0; top: 690px; width: 1200px; height: 86px;
    background: var(--black); color: var(--lime);
    text-align: center; font-size: 25px; line-height: 31px;
    padding-top: 12px;
  }
  .contact {
    position: absolute; left: 40px; top: 796px; color: var(--white);
    text-shadow: 1px 2px 4px rgba(0,0,0,0.25);
  }
  .contact-label { font-size: 38px; line-height: 40px; }
  .contact-phone { font-size: 58px; line-height: 60px; }
  .website {
    position: absolute; left: 378px; top: 856px; color: var(--white);
    font-size: 29px; text-shadow: 1px 2px 4px rgba(0,0,0,0.25);
  }
  .social-badge {
    position: absolute; left: 933px; top: 815px; width: 233px; height: 73px;
    background: var(--white); border-radius: 10px;
    display: flex; align-items: center; gap: 12px; padding: 0 14px;
  }
  .social-square { width: 44px; height: 44px; background: var(--ink); flex: none; }
  .social-text { color: var(--ink); font-size: 24px; line-height: 24px; }
</style>
</head>
<body>
<main class="flyer">
  <div class="hero-deck" role="img" aria-label="Photograph of a timber deck with evenly spaced boards, fading into green"></div>

  <div class="brand">
    <div class="brand-square"></div>
    <div class="brand-name">
      <span class="line-one">CRISP PLANKWORKS</span>
      <span class="line-two">GROUP</span>
    </div>
  </div>

  <h1 class="services">
    DECKS • STAIRS • PERGOLAS<br>
    PRIVACY SCREENS • DECK MAINTENANCE
  </h1>

  <section class="gallery">
    <div class="photo photo-pool-deck" role="img" aria-label="Photo of a timber deck around a backyard pool"></div>
    <div class="photo photo-pool-walk" role="img" aria-label="Photo of a timber walkway beside a pool with glass fencing"></div>
    <div class="photo photo-plunge" role="img" aria-label="Photo of a plunge pool surrounded by timber decking and sandstone"></div>
    <div class="photo photo-stairs" role="img" aria-label="Photo of timber stairs with a railing among garden plants"></div>
  </section>

  <div class="offer-band">
    WE WILL &nbsp;BEAT ANY REPUTABLE DECKING COMPANIES QUOTE &nbsp;BY 10%.<br>
    OUR DECKS ADD STYLE, CLASS, LONGEVITY AND PRACTICALITY TO ANY HOME.
  </div>

  <div class="contact">
    <div class="contact-label">CONTACT GORDON</div>
    <div class="contact-phone">0438261507</div>
  </div>

  <div class="website">www.crispplankworksgroup.com.au</div>

  <div class="social-badge">
    <div class="social-square"></div>
    <div class="social-text">LIKE US ON<br>PAGEBOARD</div>
  </div>
</main>
</body>
</html>
```